Namibia currently imports 60% of its food. Meridale Field Trust is an initiative which will assist Namibia to become self sustainable in terms of food production. We aim to do this through the development of 3 agricultural production zones which will include farming zones, local farmer assistance, processing and distribution of the final products. Please see our project overview attached.

```html
<!DOCTYPE html>
<html lang="en">
<head>
<meta charset="utf-8">
<title>Meridale Field Trust</title>
<link href="https://fonts.googleapis.com/css2?family=Nunito:wght@500;600;700&family=Tinos:wght@400;700&display=swap" rel="stylesheet">
<style>
  :root{
    --navy:#0b3a45;
    --green:#0f6b3a;
    --tan:#c4a383;
    --ink:#111;
    --white:#fff;
    --rule:#c9c9c9;
  }
  *{box-sizing:border-box;margin:0;padding:0}
  html,body{width:1200px;height:1029px;overflow:hidden;background:var(--white)}
  body{position:relative;font-family:"Nunito",sans-serif;color:var(--ink)}
  .hero{position:absolute;left:0;top:0;width:1200px;height:610px}
  .hero-art{position:absolute;inset:0}
  .nav{position:absolute;left:144px;top:27px;display:flex;gap:0}
  .nav a{font-size:12.5px;font-weight:700;color:var(--navy);text-decoration:none;position:absolute;white-space:nowrap}
  .pill{display:flex;align-items:center;justify-content:space-between;border-radius:30px;text-decoration:none;font-weight:700;position:absolute}
  .pill .arrow{width:22px;height:22px;border-radius:50%;display:flex;align-items:center;justify-content:center}
  .contact{left:931px;top:16px;width:127px;height:39px;background:var(--navy);color:var(--white);font-size:12px;padding:0 6px 0 22px}
  .contact .arrow{background:var(--tan)}
  .brand{position:absolute;left:0;width:1200px;top:150px;display:flex;justify-content:center;align-items:center;gap:12px}
  .brand-dot{width:16px;height:16px;border-radius:50%;background:var(--green)}
  .brand-name{font-family:"Tinos",serif;font-weight:400;font-size:42px;color:var(--green);letter-spacing:1px}
  .tagline{position:absolute;left:0;width:1200px;top:282px;text-align:center;font-family:"Tinos",serif;font-weight:700;font-size:22px;color:#111}
  .hero-btn{top:326px;width:164px;height:46px;background:var(--white);color:var(--navy);font-size:12px;padding:0 11px 0 21px}
  .hero-btn .arrow{width:27px;height:27px;background:var(--green)}
  .portrait{position:absolute;left:187px;top:634px;width:326px;height:326px;border-radius:50%;background:radial-gradient(circle at 40% 40%,#7aa35a,#3d6b2c 70%,#2c4f22)}
  .about{position:absolute;left:577px;top:652px;width:490px}
  .about h2{font-family:"Tinos",serif;font-weight:700;font-size:36px;line-height:42px;color:var(--green)}
  .about h2 .accent{color:var(--tan)}
  .about p{font-size:12px;line-height:22.5px;margin-top:0;font-weight:500}
  .about p:first-of-type{margin-top:14px}
  .about p + p{margin-top:4px}
  .explore{left:0;top:225px;width:155px;height:39px;background:var(--green);color:var(--white);font-size:12px;padding:0 8px 0 20px}
  .explore .arrow{background:var(--tan)}
  .footer{position:absolute;left:141px;top:985px;width:919px;border-top:1px solid var(--rule);text-align:center;font-size:12px;padding-top:12px;font-weight:500}
</style>
</head>
<body>
  <header class="hero">
    <svg class="hero-art" width="1200" height="610" viewBox="0 0 1200 610" role="img" aria-label="Sunlit field of young green crop rows under a bright cloudy sky">
      <defs>
        <linearGradient id="sky" x1="0" y1="0" x2="0" y2="1">
          <stop offset="0" stop-color="#eef1ee"/>
          <stop offset="0.38" stop-color="#fbf5da"/>
          <stop offset="0.45" stop-color="#e9e58a"/>
          <stop offset="0.6" stop-color="#9cc83a"/>
          <stop offset="1" stop-color="#4e8a22"/>
        </linearGradient>
      </defs>
      <rect width="1200" height="610" fill="url(#sky)"/>
      <path d="M0 593 C120 540 220 515 310 517 C430 520 520 560 640 592 C760 620 880 612 980 600 C1080 585 1160 560 1200 540 L1200 610 L0 610 Z" fill="#fff"/>
    </svg>
    <nav class="nav">
      <a href="#" style="left:0">Home</a>
      <a href="#" style="left:58px">Namibia Needs</a>
      <a href="#" style="left:172px">Solutions</a>
      <a href="#" style="left:250px">Sustainability</a>
      <a href="#" style="left:354px">Education</a>
    </nav>
    <a class="pill contact" href="#">Contact Us <span class="arrow"><svg width="8" height="10" viewBox="0 0 8 10"><path d="M2 1l4 4-4 4" stroke="#fff" stroke-width="1.2" fill="none"/></svg></span></a>
    <div class="brand"><span class="brand-dot"></span><span class="brand-name">MERIDALE FIELD TRUST</span></div>
    <h1 class="tagline">AN KVR AGRI-TECH, FOOD SECURITY INITIATIVE</h1>
    <a class="pill hero-btn" href="#" style="left:425px">Namibia Needs <span class="arrow"><svg width="8" height="10" viewBox="0 0 8 10"><path d="M2 1l4 4-4 4" stroke="#fff" stroke-width="1.2" fill="none"/></svg></span></a>
    <a class="pill hero-btn" href="#" style="left:612px">Sustainability <span class="arrow"><svg width="8" height="10" viewBox="0 0 8 10"><path d="M2 1l4 4-4 4" stroke="#fff" stroke-width="1.2" fill="none"/></svg></span></a>
  </header>

  <div class="portrait" role="img" aria-label="Farmer in a maize field checking a tablet"></div>

  <section class="about">
    <h2>ABOUT<br>MERIDALE FIELD <span class="accent">TRUST</span></h2>
    <p>Namibia currently imports 60% of its food. Meridale Field Trust is an initiative which will assist Namibia to become self sustainable in terms of food production.</p>
    <p>We aim to do this through the development of 3 agricultural production zones which will include farming zones, local farmer assistance, processing and distribution of the final products.</p>
    <a class="pill explore" href="#">Explore Our Site <span class="arrow"><svg width="8" height="10" viewBox="0 0 8 10"><path d="M2 1l4 4-4 4" stroke="#fff" stroke-width="1.2" fill="none"/></svg></span></a>
  </section>

  <footer class="footer">© 2024 Meridale Field Trust. All Rights Reserved.</footer>
</body>
</html>
```